Poly Bag for Lollies 250g size

Design a graphic for a Bag of Confectionery that can be used for many different lines. Description to be Ink jetted on by manufacturer .Image attached For reference only as Brand is Sweet Harbor.
Bag to be solid back colour
Window in front
Weight area on RHS Bottom
Brand across top section
Maybe a Graphic or Cartoon caricature on LHS to make fun..

Target Market(s)

Retail

Industry/Entity Type

Retail

Font styles to use
Sans Serif
Script

Requirements
Must have
• Window
area for Injetting
weight on front
Nice to have
• Bright Colours

```html
<!DOCTYPE html>
<html lang="en">
<head>
<meta charset="utf-8">
<title>Sweet Harbor – Lolly Bag 250g</title>
<link rel="stylesheet" href="https://fonts.googleapis.com/css2?family=Lilita+One&family=Roboto:wght@400&display=swap">
<style>
  :root {
    --galaxy-pink: #e05cc8;
    --galaxy-magenta: #c13fb4;
    --galaxy-violet: #8a4fd6;
    --galaxy-blue: #6a7fe6;
    --galaxy-deep: #5a3cc9;
    --galaxy-blush: #f1b6e0;
    --sparkle: rgba(255, 255, 255, 0.9);
    --sparkle-soft: rgba(255, 255, 255, 0.5);
    --badge-light: #f7e6f4;
    --badge-shade: #8c7d8c;
    --badge-edge: #c8323c;
    --mascot-yellow: #f2c23a;
    --mascot-red: #e0434b;
    --ink-dark: #2b1b2f;
  }
  html, body {
    margin: 0;
    padding: 0;
    width: 966px;
    height: 1200px;
    overflow: hidden;
    background: #ffffff;
  }
  .bag-face {
    position: relative;
    width: 966px;
    height: 1200px;
    overflow: hidden;
  }
  .galaxy-print {
    position: absolute;
    inset: 0;
    background:
      radial-gradient(circle at 10px 12px, var(--sparkle) 1.4px, transparent 2.2px) 0 0 / 37px 41px,
      radial-gradient(circle at 22px 6px, var(--sparkle-soft) 1px, transparent 1.8px) 0 0 / 23px 29px,
      radial-gradient(circle at 40px 50px, var(--sparkle) 2px, transparent 3px) 0 0 / 89px 97px,
      radial-gradient(circle at 5px 30px, var(--sparkle-soft) 0.8px, transparent 1.5px) 0 0 / 17px 19px,
      radial-gradient(ellipse 380px 300px at 820px 180px, var(--galaxy-magenta) 0%, transparent 70%),
      radial-gradient(ellipse 420px 300px at 150px 120px, var(--galaxy-blush) 0%, transparent 70%),
      radial-gradient(ellipse 380px 260px at 180px 420px, var(--galaxy-blue) 0%, transparent 70%),
      radial-gradient(ellipse 420px 300px at 800px 700px, var(--galaxy-pink) 0%, transparent 70%),
      radial-gradient(ellipse 400px 280px at 140px 760px, var(--galaxy-blush) 0%, transparent 70%),
      radial-gradient(ellipse 500px 320px at 300px 1080px, var(--galaxy-deep) 0%, transparent 70%),
      radial-gradient(ellipse 420px 280px at 820px 1040px, var(--galaxy-violet) 0%, transparent 70%),
      linear-gradient(170deg, var(--galaxy-pink), var(--galaxy-violet) 55%, var(--galaxy-deep));
  }
  .promo-badge {
    position: absolute;
    left: 243px;
    top: 190px;
    width: 470px;
    height: 470px;
  }
  .brand-name {
    position: absolute;
    left: 0;
    right: 0;
    top: 680px;
    margin: 0;
    text-align: center;
    font-family: "Lilita One", sans-serif;
    font-weight: 400;
    font-size: 108px;
    line-height: 104px;
    letter-spacing: 2px;
    color: var(--ink-dark);
  }
  .net-weight {
    position: absolute;
    left: 600px;
    top: 1068px;
    margin: 0;
    font-family: "Roboto", sans-serif;
    font-size: 23px;
    letter-spacing: 1px;
    color: var(--ink-dark);
  }
</style>
</head>
<body>
  <main class="bag-face">
    <div class="galaxy-print" role="img" aria-label="Sparkling pink, purple and blue galaxy print with stars"></div>

    <svg class="promo-badge" viewBox="0 0 510 510">
      <defs>
        <radialGradient id="badge-fill" cx="50%" cy="50%" r="50%">
          <stop offset="0%" stop-color="var(--badge-light)"/>
          <stop offset="62%" stop-color="var(--badge-light)"/>
          <stop offset="100%" stop-color="var(--badge-shade)"/>
        </radialGradient>
        <radialGradient id="mascot-fill" cx="50%" cy="50%" r="50%">
          <stop offset="0%" stop-color="var(--mascot-yellow)"/>
          <stop offset="70%" stop-color="var(--mascot-yellow)" stop-opacity="0.8"/>
          <stop offset="100%" stop-color="var(--mascot-red)" stop-opacity="0.35"/>
        </radialGradient>
        <path id="badge-spike" d="M255 0 L227 50 L283 50 Z"/>
      </defs>
      <g class="badge-starburst" fill="url(#badge-fill)" stroke="var(--badge-edge)" stroke-width="1">
        <use href="#badge-spike" transform="rotate(0 255 255)"/>
        <use href="#badge-spike" transform="rotate(15 255 255)"/>
        <use href="#badge-spike" transform="rotate(30 255 255)"/>
        <use href="#badge-spike" transform="rotate(45 255 255)"/>
        <use href="#badge-spike" transform="rotate(60 255 255)"/>
        <use href="#badge-spike" transform="rotate(75 255 255)"/>
        <use href="#badge-spike" transform="rotate(90 255 255)"/>
        <use href="#badge-spike" transform="rotate(105 255 255)"/>
        <use href="#badge-spike" transform="rotate(120 255 255)"/>
        <use href="#badge-spike" transform="rotate(135 255 255)"/>
        <use href="#badge-spike" transform="rotate(150 255 255)"/>
        <use href="#badge-spike" transform="rotate(165 255 255)"/>
        <use href="#badge-spike" transform="rotate(180 255 255)"/>
        <use href="#badge-spike" transform="rotate(195 255 255)"/>
        <use href="#badge-spike" transform="rotate(210 255 255)"/>
        <use href="#badge-spike" transform="rotate(225 255 255)"/>
        <use href="#badge-spike" transform="rotate(240 255 255)"/>
        <use href="#badge-spike" transform="rotate(255 255 255)"/>
        <use href="#badge-spike" transform="rotate(270 255 255)"/>
        <use href="#badge-spike" transform="rotate(285 255 255)"/>
        <use href="#badge-spike" transform="rotate(300 255 255)"/>
        <use href="#badge-spike" transform="rotate(315 255 255)"/>
        <use href="#badge-spike" transform="rotate(330 255 255)"/>
        <use href="#badge-spike" transform="rotate(345 255 255)"/>
      </g>
      <circle cx="255" cy="255" r="208" fill="url(#badge-fill)"/>
      <ellipse class="mascot-art" cx="255" cy="250" rx="170" ry="130" fill="url(#mascot-fill)"
               role="img" aria-label="Cartoon candy mascot in a Santa hat holding two candy canes"/>
    </svg>

    <h1 class="brand-name">Sweet<br>Harbor</h1>

    <p class="net-weight">Weight 250gm</p>
  </main>
</body>
</html>
```